Industry / Entity Type

Financial consultancy / advisers

Current site is: http://www.brookvale-partners.com

Looking for a complete overhaul of this site, we are after a clean modern look. Will require the ability to easily add, update and remove content, hence the WordPress design.
Example:
Add case studies
Industry documentation (downloadable brochures / flyers and such)

What we like from our current site is the colour the fonts and the logo (the city of London) we would like to have other city outlines (NYC and Tokyo, Hong Kong, Singapore).

The site will be used by our potential clients to get in contact and re-view the case studies, if possible would like to have a client login area where they can download our documents like NDA’s etc and T&C’s.

Task Outline

Create a Web Design (Coded - Design and coding required)
Designer must provide full implementation/coding depending on the platform chosen by the client (i.e. WordPress theme, HTML/CSS, bootstrap etc.)

Task Description

I need a full website built that must work on desktop and mobile. I can provide the London city skyline and the font file, which we have used. Some stock industrial photos will be required.

Requirements:

*Splash page
*What We Do
*How We do it
*Who Are We? To have the same information and links as the current site
*Why use us?
*Clients: To have the same information and links as the current site
*Partners: To have the same information and links as the current site
*Contact:

Target Market(s)

Financial institutions trading Equities, Futures, Options, Forex and Fixed Income.
Regulators, Exchanges, ECN’s
Buy side firms and Sell side firms

Industry/Entity Type

Financial

Coding

Coded - Design and coding required

Number of Pages Required

5+ page

Font styles to use
Sans Serif

Colors
f04a50

Requirements
Must have
• Splash page
• What We Do
• How We do it
• Who Are We? To have the same information and links as the current site
• Why use us?
• Clients: To have the same information and links as the current site
• Partners: To have the same information and links as the current site
• Contact:

```html
<!DOCTYPE html>
<html lang="en">
<head>
<meta charset="utf-8">
<title>Brookvale Partners – Home</title>
<link rel="stylesheet" href="https://fonts.googleapis.com/css2?family=Alegreya+Sans:wght@400;500&family=Michroma&display=swap">
<style>
  :root {
    --brand-red: #f04a50;
    --brand-red-veil: rgba(232, 84, 100, 0.82);
    --ink: #1f1f1f;
    --header-bg: #fafafa;
    --header-rule: #e6e6e6;
    --footer-bg: #1b1b1b;
    --white: #ffffff;
    --sky-top: #6f92d2;
    --sky-mid: #9fb6e2;
    --cloud: rgba(255, 255, 255, 0.75);
    --glass-violet: #7d7aa6;
    --glass-deep: #4e5f93;
    --copper: #c08a55;
    --steel: #9a8f86;
  }
  * { margin: 0; padding: 0; box-sizing: border-box; }
  html, body { width: 1200px; height: 522px; overflow: hidden; background: var(--white); }
  body {
    position: relative;
    font-family: "Alegreya Sans", Arial, sans-serif;
    color: var(--ink);
  }

  /* Header */
  .site-header {
    position: absolute; left: 0; top: 0; width: 1200px; height: 95px;
    background: var(--header-bg);
    border-bottom: 1px solid var(--header-rule);
  }
  .brand {
    position: absolute; left: 129px; top: 12px; width: 240px; height: 72px;
    display: flex; align-items: center; gap: 14px;
    text-decoration: none; color: var(--ink);
  }
  .brand-mark { width: 34px; height: 34px; border-radius: 50%; background: var(--ink); flex: none; }
  .brand-name {
    display: flex; flex-direction: column;
    font-size: 22px; font-weight: 500; letter-spacing: 4px; text-transform: uppercase; line-height: 1.05;
  }

  .top-bar {
    position: absolute; top: 18px; left: 486px; right: 126px; height: 18px;
    display: flex; align-items: center; font-size: 11px; font-weight: 500;
  }
  .contact-item { display: flex; align-items: center; gap: 4px; margin-right: 14px; }
  .contact-item svg { width: 11px; height: 11px; fill: var(--ink); }
  .social-list { display: flex; gap: 24px; margin-left: 10px; list-style: none; }
  .social-dot { display: block; width: 12px; height: 12px; border-radius: 50%; background: var(--ink); }
  .account-links { display: flex; gap: 16px; list-style: none; margin-left: auto; }
  .account-links a { color: var(--ink); text-decoration: none; }

  .main-nav {
    position: absolute; top: 62px; left: 486px; right: 126px;
    display: flex; align-items: center; list-style: none;
    font-size: 14.5px; font-weight: 500; letter-spacing: 1px;
  }
  .main-nav li { margin-right: 27px; }
  .main-nav li:nth-last-child(2) { margin-right: 0; }
  .main-nav a { color: var(--ink); text-decoration: none; }
  .main-nav .is-current a { color: var(--brand-red); }
  .main-nav .search { margin: 0 0 0 auto; }
  .main-nav .search svg { width: 15px; height: 15px; display: block; }

  /* Hero */
  .hero {
    position: absolute; left: 0; top: 95px; width: 1200px; height: 381px; overflow: hidden;
  }
  .hero-photo {
    position: absolute; inset: 0;
    background:
      radial-gradient(ellipse 110px 70px at 590px 60px, var(--cloud) 0%, rgba(255,255,255,0) 100%),
      radial-gradient(ellipse 330px 420px at 1130px 260px, var(--glass-violet) 0%, rgba(125,122,166,0.85) 45%, rgba(125,122,166,0) 100%),
      radial-gradient(ellipse 260px 380px at 40px 280px, var(--copper) 0%, rgba(192,138,85,0.8) 40%, rgba(192,138,85,0) 100%),
      radial-gradient(ellipse 220px 140px at 150px 20px, rgba(78,95,147,0.8) 0%, rgba(78,95,147,0) 100%),
      radial-gradient(ellipse 320px 200px at 640px 400px, rgba(154,143,134,0.85) 0%, rgba(154,143,134,0) 100%),
      linear-gradient(180deg, var(--sky-top) 0%, var(--sky-mid) 75%, #c3cfe8 100%);
  }
  .hero-card {
    position: absolute; left: 187px; top: 158px; width: 577px; height: 105px;
    background: var(--brand-red-veil);
    padding: 20px 18px 0 18px;
    color: var(--white);
  }
  .hero-title {
    font-family: "Michroma", Arial, sans-serif;
    font-weight: 400; font-size: 17px; letter-spacing: 3px; line-height: 1; white-space: nowrap;
  }
  .hero-lede {
    margin-top: 16px; font-size: 14px; line-height: 19px; letter-spacing: 0.8px; font-weight: 500;
  }

  /* Footer */
  .site-footer {
    position: absolute; left: 0; top: 476px; width: 1200px; height: 46px;
    background: var(--footer-bg); color: var(--white);
    display: flex; align-items: center; padding: 0 126px;
  }
  .copyright { font-size: 11.5px; font-weight: 500; }
  .site-footer .social-list { margin-left: auto; gap: 22px; }
  .site-footer .social-dot { width: 14px; height: 14px; background: var(--white); }
</style>
</head>
<body>
  <header class="site-header">
    <a class="brand" href="http://www.brookvale-partners.com">
      <span class="brand-mark" aria-hidden="true"></span>
      <span class="brand-name"><span>Brookvale</span><span>Partners</span></span>
    </a>

    <div class="top-bar">
      <span class="contact-item">
        <svg viewBox="0 0 16 16" aria-hidden="true"><path d="M3.6 1.2l2.4 2.6-1.4 2.1c.9 2 2.5 3.6 4.5 4.5l2.1-1.4 2.6 2.4-1.3 2.6C6.9 14 2 9.1 1 3.5z"/></svg>
        +44(0)20 7946 0381.
      </span>
      <span class="contact-item">
        <svg viewBox="0 0 16 16" aria-hidden="true"><path d="M1 3h14v1.4L8 9 1 4.4z M1 6l7 4.6L15 6v7H1z"/></svg>
        admin@brookvale-partners.com
      </span>
      <ul class="social-list" aria-label="Social profiles">
        <li><span class="social-dot" role="img" aria-label="Social profile 1"></span></li>
        <li><span class="social-dot" role="img" aria-label="Social profile 2"></span></li>
        <li><span class="social-dot" role="img" aria-label="Social profile 3"></span></li>
      </ul>
      <ul class="account-links">
        <li><a href="#">Clients</a></li>
        <li><a href="#">Partners</a></li>
        <li><a href="#">Login</a></li>
      </ul>
    </div>

    <ul class="main-nav">
      <li class="is-current"><a href="#">Home</a></li>
      <li><a href="#">What We Do</a></li>
      <li><a href="#">How We do it</a></li>
      <li><a href="#">Who Are We</a></li>
      <li><a href="#">Why use us?</a></li>
      <li><a href="#">Contact</a></li>
      <li class="search">
        <svg viewBox="0 0 16 16" aria-label="Search" role="img"><circle cx="9.5" cy="6.5" r="5" fill="none" stroke="#1f1f1f" stroke-width="1.4"/><line x1="6" y1="10" x2="1" y2="15" stroke="#1f1f1f" stroke-width="1.6"/></svg>
      </li>
    </ul>
  </header>

  <section class="hero">
    <div class="hero-photo" role="img" aria-label="Upward view of glass and steel office towers in the City of London against a blue sky with light clouds"></div>
    <div class="hero-card">
      <h1 class="hero-title">Brookvale Partners</h1>
      <p class="hero-lede">Brookvale is dedicated to seeing you choose the right technology strategy, ensuring you maintain a competitive edge over your peers.</p>
    </div>
  </section>

  <footer class="site-footer">
    <p class="copyright">Copyright © 2017 Brookvale Partners.</p>
    <ul class="social-list" aria-label="Social profiles">
      <li><span class="social-dot" role="img" aria-label="Social profile 1"></span></li>
      <li><span class="social-dot" role="img" aria-label="Social profile 2"></span></li>
      <li><span class="social-dot" role="img" aria-label="Social profile 3"></span></li>
    </ul>
  </footer>
</body>
</html>
```